Business Card design for new private practice opening

I need a business card design for my new private practice with my new logo uploaded as a file
On the front the logo
On the back: maybe a small logo somewhere?
Priv. Doz. DDr. Corinna Vestaluk
Fachärztin für Allgemein- & Viszeralchirurgie
Address: xxx
Tel: xxx
Mobil:xxx
Webseite:xxx
Email:xxx

Contact Information for Business Card

See project description above for details

Requirements
Nice to have
• I would like the colors of the logo incorporated into the business card

```html
<!DOCTYPE html>
<html lang="de">
<head>
<meta charset="utf-8">
<title>Vestaluk Chirurgie – Visitenkarte</title>
<link rel="stylesheet" href="https://fonts.googleapis.com/css2?family=Lexend:wght@400;600;700&display=swap">
<style>
  :root {
    --teal: #42bab4;
    --white: #ffffff;
    --grey: #7b7b7b;
    --grey-soft: #8a8a8a;
    --canvas: #e9e9e9;
  }
  * { box-sizing: border-box; margin: 0; padding: 0; }
  html, body { width: 1200px; height: 1200px; overflow: hidden; }
  body {
    background: var(--canvas);
    font-family: "Lexend", sans-serif;
    position: relative;
  }
  .card {
    position: absolute;
    left: 150px;
    width: 900px;
    height: 513px;
    overflow: hidden;
  }
  .card--front { top: 68px; background: var(--white); }
  .card--back { top: 619px; background: var(--teal); }

  /* front */
  .band {
    position: absolute;
    left: 0; top: 42px;
    width: 819px; height: 333px;
    background: var(--teal);
    border-radius: 0 166px 166px 0;
  }
  .seal {
    position: absolute;
    left: 539px; top: 70px;
    width: 280px; height: 280px;
    border-radius: 50%;
    background: var(--white);
    display: flex; align-items: center; justify-content: center;
  }
  .seal__name {
    font-weight: 700;
    font-size: 36px;
    color: var(--teal);
    letter-spacing: 1px;
  }
  .specialty {
    position: absolute;
    left: 62px; top: 90px;
    color: var(--white);
    font-weight: 600;
    font-size: 27px;
    line-height: 37px;
    text-transform: uppercase;
  }
  .icon-strip {
    position: absolute;
    left: 55px; top: 207px;
    width: 32px; height: 168px;
    background: var(--white);
  }
  .contact {
    position: absolute;
    left: 0; top: 0;
    width: 100%;
  }
  .contact__row {
    position: absolute;
    left: 55px;
    height: 32px;
    display: flex; align-items: center;
  }
  .contact__icon {
    width: 32px; display: flex; justify-content: center;
  }
  .contact__icon svg { fill: var(--grey); }
  .contact__text {
    margin-left: 10px;
    color: var(--white);
    font-size: 24px;
    letter-spacing: 0.5px;
  }
  .address {
    position: absolute;
    left: 55px; top: 398px;
    display: flex;
  }
  .address__icon {
    width: 30px; height: 30px;
    background: var(--grey);
    display: flex; align-items: center; justify-content: center;
    margin-left: 1px;
  }
  .address__text {
    margin-left: 11px;
    color: var(--grey-soft);
    font-size: 24px;
    line-height: 35px;
    margin-top: -3px;
    letter-spacing: 0.5px;
  }

  /* back */
  .pill {
    position: absolute;
    left: 106px; top: 134px;
    width: 690px; height: 247px;
    background: var(--white);
    border-radius: 124px;
  }
  .brand-dot {
    position: absolute;
    left: 209px; top: 184px;
    width: 144px; height: 144px;
    border-radius: 50%;
    background: var(--teal);
  }
  .brand-name {
    position: absolute;
    left: 372px; top: 205px;
    color: var(--grey);
    font-weight: 600;
    font-size: 56px;
    line-height: 62px;
    letter-spacing: 1px;
  }
</style>
</head>
<body>
  <section class="card card--front">
    <div class="band"></div>
    <div class="seal"><span class="seal__name">VESTALUK</span></div>
    <h1 class="specialty">Fachärztin für Allgemein<br>&amp; Viszeralchirurgie</h1>
    <div class="icon-strip"></div>
    <div class="contact">
      <div class="contact__row" style="top:236px">
        <span class="contact__icon"><svg width="16" height="16" viewBox="0 0 24 24"><path d="M6.6 10.8a15 15 0 0 0 6.6 6.6l2.2-2.2c.3-.3.7-.4 1-.2 1.1.4 2.3.6 3.6.6.6 0 1 .4 1 1V20c0 .6-.4 1-1 1A17 17 0 0 1 3 4c0-.6.4-1 1-1h3.5c.6 0 1 .4 1 1 0 1.3.2 2.5.6 3.6.1.3 0 .7-.2 1z"/></svg></span>
        <span class="contact__text">(610) 000-0000</span>
      </div>
      <div class="contact__row" style="top:273px">
        <span class="contact__icon"><svg width="14" height="20" viewBox="0 0 14 20"><path d="M2 0h10a2 2 0 0 1 2 2v16a2 2 0 0 1-2 2H2a2 2 0 0 1-2-2V2a2 2 0 0 1 2-2zm0 3v12h10V3z"/></svg></span>
        <span class="contact__text">(610) 000-0000</span>
      </div>
      <div class="contact__row" style="top:308px">
        <span class="contact__icon"><svg width="18" height="14" viewBox="0 0 18 14"><path d="M0 0h18v14H0zM1.5 1.5 9 7l7.5-5.5z"/></svg></span>
        <span class="contact__text">www.vestaluk-praxis.com</span>
      </div>
    </div>
    <div class="address">
      <span class="address__icon"><svg width="14" height="18" viewBox="0 0 14 18"><path fill="#fff" d="M7 0a7 7 0 0 1 7 7c0 5-7 11-7 11S0 12 0 7a7 7 0 0 1 7-7zm0 4.5A2.5 2.5 0 1 0 7 9.5a2.5 2.5 0 0 0 0-5z"/></svg></span>
      <p class="address__text">0/2 Orrin Blvd Suite 0000,<br>Maple Fork, PA 11111</p>
    </div>
  </section>

  <section class="card card--back">
    <div class="pill"></div>
    <div class="brand-dot"></div>
    <p class="brand-name">VESTALUK<br>CHIRURGIE</p>
  </section>
</body>
</html>
```